Music Industry Business Needs a Business Card Design

Copper Lantern is an audio mastering company that has been in business for 20 years. Mastering is the final creative step in the music production chain. Our job is to make the music sound as good as it possibly can prior to release to the public. Our world is technical, artistic, precise. We work on everything from independent artists to the music for the Grandfield Cup. We are looking for a new, more modern business card design. I am uploading a copy of our logo, although it doesn't absolutely need to be included in the design.

Target Market(s)

Music Industry Professionals

Industry/Entity Type

Business

Contact Information for Business Card

Address, Phone, Email, Website, Name, Job Title

Font styles to use
Sans Serif

Requirements
Must have
• Sorry, but I don't have any concrete things to request. If I had a clear idea of what I want, I would probably just design something myself. I am looking for fresh input and thought I would try this.
Should not have
• Anything that is typical, such as headphones or the like.

```html
<!DOCTYPE html>
<html lang="en">
<head>
<meta charset="utf-8">
<title>Copper Lantern – Business Card</title>
<link rel="stylesheet" href="https://fonts.googleapis.com/css2?family=Questrial&display=swap">
<style>
  :root {
    --page: #2a2c2e;
    --card: #0c0c0d;
    --cyan-a: #4fd6f4;
    --cyan-b: #7ff3ff;
    --magenta-a: #f21de0;
    --magenta-b: #f77cec;
    --lime-a: #dff55a;
    --lime-b: #c6f53a;
    --orange-a: #ffb42e;
    --orange-b: #ff8a12;
    --band-a: #1b4d6e;
    --band-b: #1f8a80;
    --ink: #ffffff;
  }
  * { box-sizing: border-box; margin: 0; padding: 0; }
  html, body { width: 1200px; height: 1000px; overflow: hidden; }
  body {
    background: var(--page);
    font-family: "Questrial", sans-serif;
    color: var(--ink);
    position: relative;
  }
  .card {
    position: absolute;
    left: 150px; top: 240px;
    width: 900px; height: 520px;
    background: var(--card);
    border-radius: 4px;
  }
  .tile { position: absolute; }
  .tile--brand {
    left: 290px; top: 30px; width: 400px; height: 170px;
    background: linear-gradient(120deg, var(--cyan-a), var(--cyan-b));
    display: flex; align-items: center; justify-content: center; gap: 12px;
  }
  .brand-dot {
    width: 12px; height: 12px; border-radius: 50%;
    background: var(--ink);
  }
  .brand-name {
    font-size: 26px; letter-spacing: 3px; text-transform: uppercase;
    color: var(--ink);
  }
  .tile--icons {
    left: 60px; top: 110px; width: 220px; height: 330px;
    background: linear-gradient(160deg, var(--magenta-a), var(--magenta-b));
    display: flex; flex-direction: column; align-items: flex-end;
    justify-content: flex-start; gap: 16px; padding: 30px 28px;
  }
  .tile--icons svg { width: 34px; height: 30px; fill: var(--ink); }
  .tile--contact {
    left: 290px; top: 210px; width: 400px; height: 230px;
    background: linear-gradient(160deg, var(--lime-a), var(--lime-b));
    padding: 30px 34px;
    display: flex; flex-direction: column; gap: 10px;
    font-size: 28px; letter-spacing: 1px;
  }
  .tile--person {
    left: 700px; top: 150px; width: 170px; height: 230px;
    background: linear-gradient(150deg, var(--orange-a), var(--orange-b));
    padding: 30px 18px;
    display: flex; flex-direction: column; align-items: flex-end; text-align: right;
  }
  .person-name { font-size: 30px; font-weight: 400; line-height: 1.1; }
  .person-role { font-size: 20px; margin-top: 6px; }
  .band {
    position: absolute;
    left: 30px; top: 450px; width: 840px; height: 50px;
    background: linear-gradient(90deg, var(--band-a), var(--band-b));
    display: flex; align-items: center; padding-left: 240px;
    font-size: 28px; letter-spacing: 1px;
  }
</style>
</head>
<body>
  <div class="card">
    <div class="tile tile--brand">
      <span class="brand-dot"></span>
      <span class="brand-name">Copper Lantern</span>
    </div>

    <div class="tile tile--icons" aria-hidden="true">
      <svg viewBox="0 0 24 20"><path d="M12 3C6 3 1 5 1 8v2h6V8c1-1 3-1.5 5-1.5S16 7 17 8v2h6V8c0-3-5-5-11-5zM6 12h12l2 6H4z"/></svg>
      <svg viewBox="0 0 24 20"><path d="M12 1 1 10h3v9h6v-6h4v6h6v-9h3z"/></svg>
      <svg viewBox="0 0 24 20"><path d="M1 3h22v14H1zM3 5v1l9 6 9-6V5l-9 6z"/></svg>
    </div>

    <div class="tile tile--contact">
      <span class="contact-phone">555 408 2716</span>
      <span class="contact-address">48 Alder Row</span>
      <span class="contact-email">info@copperlantern.com</span>
    </div>

    <div class="tile tile--person">
      <span class="person-name">Dana Mercer</span>
      <span class="person-role">manager</span>
    </div>

    <div class="band">www.copperlantern.com</div>
  </div>
</body>
</html>
```